Non-Fiction Book Cover Series Concepts

I need front cover concepts for a non-fiction business book series. Just concepts at this stage to show to backers (full cover designs later).

The books are for leaders and business owners. A mature, sophisticated market, AND, bold and innovative.

The series needs to be extensible - the concepts need to be able to work across at least 40 books. I am happy with a colour theme, or contrasts, or icon theme, there is no limitation to the imagination.

The books need to look like they belong to a series and to also stand alone.

I prefer simple and bold.

Imagine the Heron trade series (https://www.heronbooks.example/series/tws/heron-trade-wisdom-series.html) - but I hate these designs (the colours don't work for me).

The imprint is MindfulVantagePress.example - the logo mark for the imprint is attached.

The books will be printed and ebooks - the printed version will be 5 inches by 8 inches form factor. They will be printed with a matt cover.

IF YOU WANT A BOOK TITLE TO TRY, use this:

Steady Momentum: Apply the R.A.V. Model to Inspire, Unlock and Sustain Talent

Thank you for your interest!

Target Market(s)

Business owners, leaders, entrepreneurs

Industry/Entity Type

Leadership

Font styles to use
Serif
Sans Serif

Requirements
Must have
• Extensible - the concept can work for many books and ALL books look part of the series
Nice to have
• I prefer simple, icons rather than photos
Should not have
• No photographic designs - icon, drawing

```html
<!DOCTYPE html>
<html lang="en">
<head>
<meta charset="utf-8">
<title>Business and Business – Book Cover Spread</title>
<link rel="stylesheet" href="https://fonts.googleapis.com/css2?family=Poppins:wght@400;700;800&display=swap">
<style>
  :root {
    --violet: #5e46ef;
    --green: #6cbe44;
    --white: #ffffff;
    --ink-box: rgba(25, 88, 75, 0.5);
    --art-light: #cfe3e6;
    --art-gold: #e9b52c;
  }
  html, body {
    margin: 0;
    padding: 0;
    width: 1200px;
    height: 889px;
    overflow: hidden;
    background: var(--violet);
  }
  .spread {
    position: relative;
    width: 1200px;
    height: 889px;
    overflow: hidden;
    font-family: "Poppins", sans-serif;
    color: var(--white);
  }
  .spread-shapes {
    position: absolute;
    inset: 0;
    width: 1200px;
    height: 889px;
  }
  .spread-shapes .violet { fill: var(--violet); }
  .spread-shapes .green { fill: var(--green); }
  .spread-shapes .white { fill: var(--white); }

  /* Back cover */
  .back-title {
    position: absolute;
    left: 41px;
    top: 44px;
    margin: 0;
    font-size: 32px;
    font-weight: 800;
    letter-spacing: -0.2px;
    line-height: 1;
    white-space: nowrap;
  }
  .back-blurb {
    position: absolute;
    left: 100px;
    top: 109px;
    width: 365px;
    margin: 0;
    font-size: 15px;
    font-weight: 400;
    line-height: 17px;
  }
  .back-excerpt {
    position: absolute;
    left: 81px;
    top: 371px;
    width: 388px;
    height: 246px;
    background: var(--ink-box);
    box-sizing: border-box;
    padding: 30px 24px 0 23px;
  }
  .back-excerpt p {
    margin: 0;
    font-size: 15px;
    line-height: 17px;
  }
  .back-url {
    position: absolute;
    left: 76px;
    top: 658px;
    width: 390px;
    text-align: center;
    font-size: 21px;
    font-weight: 700;
    letter-spacing: -0.2px;
    white-space: nowrap;
  }
  .imprint-name {
    position: absolute;
    display: flex;
    align-items: center;
    gap: 8px;
    font-weight: 700;
    color: var(--violet);
    white-space: nowrap;
  }
  .imprint-name .dot {
    width: 14px;
    height: 14px;
    border-radius: 50%;
    background: var(--violet);
  }
  .imprint-name.back {
    left: 77px;
    top: 738px;
    font-size: 22px;
  }
  .back-box {
    position: absolute;
    left: 306px;
    top: 729px;
    width: 223px;
    height: 132px;
    background: var(--white);
  }

  /* Spine */
  .spine-text {
    position: absolute;
    left: 583px;
    writing-mode: vertical-rl;
    font-size: 34px;
    font-weight: 800;
    line-height: 1;
    white-space: nowrap;
    letter-spacing: -0.5px;
  }
  .spine-title { top: 36px; }
  .spine-author { top: 578px; }

  /* Front cover */
  .front-title {
    position: absolute;
    left: 680px;
    top: 22px;
    width: 474px;
    margin: 0;
    text-align: center;
    font-size: 90px;
    font-weight: 800;
    line-height: 73px;
    letter-spacing: -3px;
  }
  .front-title span { display: block; }
  .front-art {
    position: absolute;
    left: 740px;
    top: 360px;
    width: 353px;
    height: 327px;
    border-radius: 50%;
    background: radial-gradient(circle at 50% 40%, var(--art-light) 0%, #8fc6a0 55%, var(--art-gold) 100%);
  }
  .front-author {
    position: absolute;
    left: 680px;
    top: 718px;
    width: 348px;
    text-align: center;
    font-size: 37px;
    font-weight: 700;
    color: var(--green);
    line-height: 1;
    letter-spacing: -0.5px;
    white-space: nowrap;
  }
  .imprint-name.front {
    left: 748px;
    top: 782px;
    font-size: 22px;
  }
  .front-url {
    position: absolute;
    left: 680px;
    top: 839px;
    width: 360px;
    text-align: center;
    font-size: 20px;
    font-weight: 700;
    color: var(--violet);
    letter-spacing: -0.3px;
    white-space: nowrap;
  }
</style>
</head>
<body>
<main class="spread">
  <svg class="spread-shapes" viewBox="0 0 1800 1334" preserveAspectRatio="none" aria-hidden="true">
    <rect class="violet" x="0" y="0" width="1800" height="1334"/>
    <rect class="green" x="0" y="615" width="833" height="719"/>
    <rect class="white" x="965" y="410" width="835" height="924"/>
    <polygon class="green" points="965,410 1800,410 1315,885 965,545"/>
    <polygon class="violet" points="965,585 1305,905 965,930"/>
    <polygon class="violet" points="1800,440 1800,1334 1750,1334 1328,908"/>
  </svg>

  <h2 class="back-title">BUSINESS AND BUSINESS</h2>
  <p class="back-blurb">Lorem ipsum dolor sit amet, consectetur adipiscing elit. Aenean sit amet risus et ante faucibus iaculis. In vitae convallis tortor. Fusce iaculis purus in risus rutrum tincidunt. Cras porttitor ex sapien, eget sodales est bibendum non. Cras scelerisque est feugiat pretium posuere. Aliquam congue magna justo, et euismod felis volutpat vitae. Integer sit amet augue finibus, sodales lectus et, rhoncus nisi. Nulla cursus sit amet neque at sagittis. Fusce eget urna lectus. Proin vitae magna vel nibh posuere rutrum. Phasellus a lobortis libero. Nullam felis lacus, aliquam id lacinia a, commodo pretium diam.</p>
  <div class="back-excerpt">
    <p>Sed non nunc maximus, tristique tellus sed, ultricies urna. Suspendisse convallis nec erat sed rhoncus. Curabitur feugiat efficitur interdum. Phasellus commodo felis nec eleifend egestas. Nullam ut convallis ligula. Curabitur accumsan ligula quam, egestas hendrerit massa accumsan quis. Curabitur laoreet dui ipsum, ac congue elit dapibus quis. Ut lacinia, est sit amet porttitor bibendum, elit lectus mollis ex, at venenatis augue lacus id augue.</p>
  </div>
  <div class="back-url">MINDFULVANTAGEPRESS.EXAMPLE</div>
  <div class="imprint-name back"><span class="dot"></span>MINDFUL VANTAGE</div>
  <div class="back-box"></div>

  <div class="spine-text spine-title">BUSINESS AND BUSINESS</div>
  <div class="spine-text spine-author">AUTHOR NAME</div>

  <h1 class="front-title"><span>BUSINESS</span><span>AND</span><span>BUSINESS</span></h1>
  <div class="front-art" role="img" aria-label="Illustration of two business people standing on stacks of gold coins beside a rising line chart, with clouds behind"></div>
  <div class="front-author">AUTHOR NAME</div>
  <div class="imprint-name front"><span class="dot"></span>MINDFUL VANTAGE</div>
  <div class="front-url">MINDFULVANTAGEPRESS.EXAMPLE</div>
</main>
</body>
</html>
```